Very visible CoWorking Building Sign overlooking downtown LA and 110 freeway

Our building is drab but very visible and in the best location. We need a great sign for our monolith that overlooks downtown LA and the 100 freeway. We are a new CoWorking business and would like to have a few things we do on the sign: private offices, virtual offices, CoWorking Lounge. Everything we have seen is ho-hum. Can you get us noticed? We need people to know what we do and that we are here but in a creative, professional, unique sign.
Target Market(s)
People who have a business in DTLA, remote workers and those who work from home who need a professional address.
Requirements
Must have
- Our logo (which can be somewhat reimagined) which has our address 2740 on it. The three things we focus on: Private Offices, Virtual Offices, CoWorking Lounge. Incorporate some Navy. Readable from several hundred feet away.
Nice to have
- Mural feel? Something inspirational in this crazy COVID times? Graphics? Color block. I like the idea of decorative but it has to be readable as a building sign. The same with the use of colors. Our colors are grays and navy but with a pop of the chartreuse (we have 2 velvet chartreuse chairs in the space). Helpful to view our website: Halvorn2740.com.
Should not have
- Not too graffiti. Keep it professional but unique and wow.

```html
<!DOCTYPE html>
<html lang="en">
<head>
<meta charset="utf-8">
<title>Halvorn 2740 Building Sign</title>
<link rel="stylesheet" href="https://fonts.googleapis.com/css2?family=Josefin+Sans:wght@400&family=Libre+Baskerville:wght@700&family=Tinos:wght@700&display=swap">
<style>
  :root {
    --backdrop: #c4c4c4;
    --navy: #0d2a4f;
    --chartreuse: #8dc63f;
    --sign-blue: #0563ae;
    --white: #ffffff;
  }
  * { margin: 0; padding: 0; box-sizing: border-box; }
  html, body {
    width: 1200px; height: 1097px; overflow: hidden;
    background: var(--backdrop);
  }
  .sign {
    position: absolute; left: 287px; top: 28px;
    width: 625px; height: 1040px;
    background: var(--navy);
    overflow: hidden;
  }
  .sign-waves { position: absolute; left: 0; top: 0; width: 625px; height: 1040px; }
  .brand {
    position: absolute; left: 70px; top: 50px; width: 480px;
    font-family: "Josefin Sans", sans-serif; font-weight: 400;
    color: var(--white); text-align: right;
  }
  .brand-name { font-size: 96px; line-height: 1; letter-spacing: 2px; }
  .brand-domain { font-size: 38px; line-height: 1; margin-top: 6px; letter-spacing: 1px; }
  .service-icon {
    position: absolute; left: 71px; width: 172px; height: 172px;
    border-radius: 50%; background: var(--chartreuse);
    border: 2px solid var(--white);
  }
  .service-label {
    position: absolute; left: 270px;
    font-family: "Libre Baskerville", serif; font-weight: 700;
    font-size: 37px; line-height: 44px; color: var(--white);
    text-transform: uppercase;
  }
  .divider {
    position: absolute; left: 286px; width: 181px; height: 2px;
    background: var(--white);
  }
  .phone {
    position: absolute; left: 0; width: 625px; top: 895px;
    text-align: center;
    font-family: "Tinos", serif; font-weight: 700;
    font-size: 104px; line-height: 1; color: var(--white);
    letter-spacing: -3px;
    transform: scaleX(0.86);
  }
</style>
</head>
<body>
  <main class="sign">
    <svg class="sign-waves" viewBox="0 0 625 1040" aria-hidden="true">
      <path fill="var(--chartreuse)" d="M0,778 C160,860 330,900 625,835 L625,885 C420,905 210,905 0,880 Z"/>
      <path fill="var(--white)" d="M0,800 C200,878 410,900 625,812 L625,842 C410,912 200,900 0,825 Z"/>
      <path fill="var(--sign-blue)" d="M0,812 C190,885 400,910 625,848 L625,1040 L0,1040 Z"/>
      <path fill="var(--sign-blue)" d="M0,760 C120,830 240,870 380,880 C220,870 100,830 0,790 Z"/>
    </svg>

    <header class="brand">
      <div class="brand-name">HALVORN</div>
      <div class="brand-domain">2740.com</div>
    </header>

    <div class="service-icon" style="top:248px" role="img" aria-label="Line icon of a private office desk with chair, lamp and framed picture"></div>
    <p class="service-label" style="top:290px">Private<br>Offices</p>
    <div class="divider" style="top:432px"></div>

    <div class="service-icon" style="top:447px" role="img" aria-label="Line icon of a reception desk with envelope and plant"></div>
    <p class="service-label" style="top:490px">Virtual<br>Offices</p>
    <div class="divider" style="top:634px"></div>

    <div class="service-icon" style="top:646px" role="img" aria-label="Line icon of people talking at a shared table"></div>
    <p class="service-label" style="top:688px">Coworking<br>Lounge</p>

    <p class="phone">213.555.0148</p>
  </main>
</body>
</html>
```